Flyer-Design für ein Hautkrebs-Präventionsprojekt
Zielgruppe
Wir sind der Gesundheitsring Baden-Württemberg. Bei diesem Projekt handelt es sich um ein Hautkrebs-Präventionsprojekt. Ein gesunder Umgang mit der Sonne soll vor allem bei Kindern, aber auch ihren Eltern und Erzieherinnen gefördert werden. Durch die sensible Kinderhaut (Schutzmechanismus noch nicht ganz entwickelt) sind Sonnenbrände im Kindheitsalter ein extremes Hautkrebsrisiko für das spätere Erwachsenenalter. Um über Möglichkeiten wie man sich schützen kann und einen gesunden Umgang mit der Sonne zu pflegen bieten wir Informationsschulungen an. Hierfür sollen die Flyer gestaltet werden.
Aufgabenstellung
Die Flyer in A6, also Postkartenformat (hoch oder quer spielt keine Rolle) sollen sich an Eltern und pädagogisches Fachpersonal richten. Unsere Vorstellung/Idee war ein 'pfiffiger', eventuell herausfordender aber auch lustiger Satz vorne, und die Einladung hinten. Inspiriert so ein bisschen von diversen Werbekarten die man in Clubs oder in der Gastronomie mitnehmen kann! Die Vorderseite soll also Aufmerksamkeit an sich ziehen und zum 'in die Hand nehmen und einpacken' bewegen.
Ansonsten ist Ihrer Kreativität keine Grenzen gesetzt.
Als Einladung soll folgender Text auf die Rückseite (inkl. Logo):
Liebe Eltern, liebe pädagogische Fachkräfte,
wir laden sie herzlich zu unserer Informationsveranstaltung über einen gesunden Umgang mit der Sonne zur Hautkrebsprävention ein.
Wann? 11.04.19 o. 11.06.19
Wo? Landesvorsorgekasse Baden-Württemberg
Lindenhofweg 28
70599 Stuttgart
Besonders Kinder haben aufgrund ihrer sensiblen Haut ein erhöhtes Schutzbedürfnis.
Nutzen Sie die Chance, sich zu informieren und Ihre Familie und sich zu schützen!
Haben Sie noch Fragen? Melden Sie sich bei uns
Gerne können anstatt wann und wo und für die Kontaktdaten kleine Symbole verwendet werden.
Wir freuen uns auf Ihre Vorschläge!
PS: Die 'Wann'-Daten können sich eventuell noch ändern

```html
<!DOCTYPE html>
<html lang="de">
<head>
<meta charset="utf-8">
<title>Flyer Hautkrebsprävention – Gesundheitsring Baden-Württemberg</title>
<link rel="stylesheet" href="https://fonts.googleapis.com/css2?family=Anton&family=Arimo:wght@400;700&display=swap">
<style>
  :root {
    --page: #ffffff;
    --purple: #9a0fd2;
    --orange: #e0743a;
    --navy: #15045c;
    --ink: #2a2850;
    --gold: #d3bb63;
    --panel: rgba(255, 255, 255, 0.62);
    --logo-ink: #3a3a3a;
    --logo-mark: #7cb84a;
    --photo-top: #8cc4ea;
    --photo-bottom: #c9ab7c;
    --photo-soft-a: #fbeee4;
    --photo-soft-b: #f3d9c6;
  }
  * { margin: 0; padding: 0; box-sizing: border-box; }
  html, body { width: 750px; height: 1200px; overflow: hidden; background: var(--page); }
  body { position: relative; font-family: "Arimo", Arial, sans-serif; }

  .card { position: absolute; overflow: hidden; }
  .card--front { left: 29px; top: 39px; width: 697px; height: 494px; }
  .card--back { left: 44px; top: 639px; width: 677px; height: 494px; background: var(--page); }

  .photo-area {
    position: absolute; inset: 0;
    background: linear-gradient(180deg, var(--photo-top) 0%, var(--photo-bottom) 100%);
  }

  .logo {
    position: absolute; display: flex; align-items: center; gap: 7px;
    color: var(--logo-ink); font-size: 9.5px; line-height: 11.5px; letter-spacing: 0.06em;
  }
  .logo__mark { width: 18px; height: 18px; background: var(--logo-mark); flex: none; }
  .card--front .logo {
    left: 537px; top: 0; width: 160px; height: 47px;
    background: var(--page); padding-left: 6px;
  }
  .card--back .logo { left: 502px; top: 12px; }

  .slogan-panel {
    position: absolute; background: var(--panel);
    font-family: "Anton", Impact, sans-serif; font-weight: 400;
  }
  .slogan-panel--envy {
    left: 17px; top: 67px; width: 334px; height: 100px;
    transform: rotate(-4deg); padding: 8px 0 0 22px;
    color: var(--purple); font-size: 44px; line-height: 38px;
  }
  .slogan-panel--spots {
    left: 26px; top: 165px; width: 340px; height: 100px;
    transform: rotate(-4deg); padding: 8px 0 0 22px;
    color: var(--orange); font-size: 46px; line-height: 40px;
  }
  .slogan-panel--protect {
    left: 23px; top: 335px; width: 472px; height: 132px;
    padding: 4px 0 0 17px; background: rgba(255,255,255,0.55);
    color: var(--navy); font-size: 60px; line-height: 60px; letter-spacing: 0.01em;
  }

  .kid-portrait {
    position: absolute; right: 0; top: 50px; width: 360px; height: 444px;
    background: linear-gradient(180deg, rgba(255,255,255,0) 0%, var(--photo-soft-a) 25%, var(--photo-soft-b) 100%);
  }
  .gold-bar { position: absolute; left: 0; top: 0; width: 14px; height: 100%; background: var(--gold); }

  .invitation { position: absolute; left: 38px; top: 53px; color: var(--ink); font-size: 17px; letter-spacing: 0.05em; }
  .invitation__greeting { font-weight: 700; line-height: 22px; }
  .invitation__text { line-height: 22px; }
  .invitation__intro { margin-top: 22px; }
  .event-details { position: absolute; left: 32px; top: 212px; color: var(--ink); font-size: 17px; font-weight: 700; line-height: 22px; letter-spacing: 0.05em; }
  .event-details__row { display: flex; }
  .event-details__label { width: 86px; flex: none; }
  .invitation__note { position: absolute; left: 38px; top: 320px; color: var(--ink); font-size: 17px; line-height: 22px; letter-spacing: 0.05em; }
  .invitation__contact { position: absolute; left: 38px; top: 430px; color: var(--ink); font-size: 17px; line-height: 22px; letter-spacing: 0.05em; }
  .invitation__contact strong { font-weight: 700; }
</style>
</head>
<body>

<section class="card card--front">
  <div class="photo-area" role="img" aria-label="Platz für Foto: Palmenstrand am Meer mit einer Giraffe mit Sonnenbrille"></div>
  <div class="logo">
    <span class="logo__mark"></span>
    <span>Gesundheitsring<br>Baden-Württemberg e.V.</span>
  </div>
  <h2 class="slogan-panel slogan-panel--envy">Sei neidisch auf<br>meinen Urlaub!</h2>
  <h2 class="slogan-panel slogan-panel--spots">Nicht auf<br>meine Flecken!</h2>
  <h1 class="slogan-panel slogan-panel--protect">Schütze dich<br>gegen Hautkrebs!</h1>
</section>

<section class="card card--back">
  <div class="kid-portrait" role="img" aria-label="Platz für verblasstes Foto: Kind mit großer Sonnenbrille in der Sonne"></div>
  <div class="gold-bar"></div>
  <div class="logo">
    <span class="logo__mark"></span>
    <span>Gesundheitsring<br>Baden-Württemberg e.V.</span>
  </div>

  <div class="invitation">
    <p class="invitation__greeting">Liebe Eltern, liebe pädagogische Fachkräfte,</p>
    <p class="invitation__text invitation__intro">wir laden sie herzlich zu unserer<br>Informationsveranstaltung über einen<br>gesunden Umgang mit der Sonne zur<br>Hautkrebsprävention ein.</p>
  </div>

  <div class="event-details">
    <div class="event-details__row"><span class="event-details__label">Wann?</span><span>11.04.2019 oder 11.06.2019</span></div>
    <div class="event-details__row"><span class="event-details__label">Wo?</span><span>Landesvorsorgekasse Stuttgart<br>Lindenhofweg 28<br>70599 Stuttgart</span></div>
  </div>

  <p class="invitation__note">Besonders Kinder haben aufgrund ihrer sensiblen<br>Haut ein erhöhtes Schutzbedürfnis.<br>Nutzen Sie die Chance sich zu informieren und<br>Ihre Familie und sich zu schützen!</p>

  <p class="invitation__contact">Haben Sie noch Fragen?<br>Melden Sie sich bei uns:<br><strong>0711 555-20480 info@gesundheitsring-bw.de</strong></p>
</section>

</body>
</html>
```